K.T.L Electrical Services Pty Ltd

Electrical contracting business. I have a base for the design which i like. The contact number needs to be changed to 0431862957 and the O made more solid and level with the rest of the letters. If you have any other ideas of what would make it better I'm happy to see them.

The back side to be written as dot points with the following:
- Residential & Commercial
- Maintenance
- PV & Battery servicing
- EV Chargers

```html
<!DOCTYPE html>
<html lang="en">
<head>
<meta charset="utf-8">
<title>K.T.L Electrical Services – Business Card</title>
<link href="https://fonts.googleapis.com/css2?family=Arimo:wght@400;700&display=swap" rel="stylesheet">
<style>
  :root {
    --page: #e9e9e9;
    --ink: #111111;
    --black: #000000;
    --teal-top: #a0bcbd;
    --teal-bottom: #8aabab;
    --teal-mark: #9fc1c1;
    --teal-faint: #b3cdcd;
    --accent: #d98a3a;
  }
  * { box-sizing: border-box; margin: 0; padding: 0; }
  html, body { width: 1200px; height: 1200px; overflow: hidden; }
  body {
    background: var(--page);
    font-family: "Arimo", Arial, sans-serif;
    color: var(--ink);
    position: relative;
  }
  .card {
    position: absolute;
    left: 262px;
    width: 680px;
    height: 390px;
    overflow: hidden;
  }
  .card-front { top: 170px; display: flex; }
  .card-back {
    top: 655px;
    background: linear-gradient(180deg, var(--teal-top), var(--teal-bottom));
    text-align: center;
  }

  /* shared brand name block */
  .brand {
    display: flex;
    align-items: center;
    gap: 12px;
  }
  .brand-dot {
    width: 40px; height: 40px;
    border-radius: 50%;
    background: currentColor;
    flex: none;
  }
  .brand-name {
    font-family: "Arimo", Arial, sans-serif;
    font-weight: 700;
    font-size: 24px;
    line-height: 28px;
    text-align: left;
  }
  .brand-licence {
    font-family: "Arimo", Arial, sans-serif;
    font-size: 14px;
    margin-top: 10px;
  }

  /* front */
  .brand-panel {
    width: 368px;
    height: 100%;
    background: var(--black);
    display: flex;
    flex-direction: column;
    align-items: center;
    justify-content: center;
    padding-bottom: 50px;
    color: var(--teal-mark);
  }
  .accent-bar { width: 9px; height: 100%; background: var(--accent); border-left: 2px solid var(--black); }
  .contact-panel {
    flex: 1;
    background: linear-gradient(180deg, var(--teal-top), var(--teal-bottom));
    padding: 92px 0 0 38px;
  }
  .person-name { font-weight: 700; font-size: 25px; letter-spacing: 0.5px; }
  .person-title { font-size: 15px; margin-top: 2px; }
  .address { font-size: 16px; line-height: 20px; margin-top: 20px; }
  .contact-list { list-style: none; margin-top: 14px; font-size: 16px; line-height: 20px; }
  .contact-list li { display: flex; align-items: center; gap: 10px; }
  .contact-list svg { width: 14px; height: 14px; flex: none; }

  /* back */
  .card-back .brand-block {
    margin-top: 92px;
    display: flex;
    flex-direction: column;
    align-items: center;
    color: var(--teal-faint);
  }
  .card-back .brand { gap: 16px; }
  .card-back .brand-dot { width: 58px; height: 58px; }
  .card-back .brand-name { font-size: 34px; line-height: 40px; }
  .card-back .brand-licence { font-size: 19px; margin-top: 12px; }
  .services { margin-top: 78px; font-size: 17px; line-height: 22px; }
  .services .sep { margin: 0 10px; }
</style>
</head>
<body>
  <section class="card card-front">
    <div class="brand-panel">
      <div class="brand">
        <span class="brand-dot"></span>
        <div class="brand-name">K.T.L Electrical<br>Services Pty Ltd</div>
      </div>
      <div class="brand-licence">EC 27418</div>
    </div>
    <div class="accent-bar"></div>
    <div class="contact-panel">
      <div class="person-name">DANIEL REEVE</div>
      <div class="person-title">President</div>
      <div class="address">214 Ridgeway Drive<br>Hillcrest, Canada 48210</div>
      <ul class="contact-list">
        <li>
          <svg viewBox="0 0 24 24" aria-hidden="true"><path fill="#111" d="M6.6 10.8a15.1 15.1 0 0 0 6.6 6.6l2.2-2.2a1 1 0 0 1 1-.25 11.4 11.4 0 0 0 3.6.57 1 1 0 0 1 1 1V20a1 1 0 0 1-1 1A17 17 0 0 1 3 4a1 1 0 0 1 1-1h3.5a1 1 0 0 1 1 1c0 1.25.2 2.450.57 3.57a1 1 0 0 1-.25 1z"/></svg>
          0431862957
        </li>
        <li>
          <svg viewBox="0 0 24 24" aria-hidden="true"><rect x="2" y="5" width="20" height="14" fill="#111"/><path d="M2 5l10 8 10-8" fill="none" stroke="#9bb7b8" stroke-width="2"/></svg>
          info@KTL.com
        </li>
        <li>
          <svg viewBox="0 0 24 24" aria-hidden="true"><circle cx="12" cy="12" r="10" fill="#111"/><path d="M12 2v20M2 12h20M5 6.5c4 2 10 2 14 0M5 17.5c4-2 10-2 14 0" fill="none" stroke="#9bb7b8" stroke-width="1.4"/></svg>
          www.KTL.com
        </li>
      </ul>
    </div>
  </section>

  <section class="card card-back">
    <div class="brand-block">
      <div class="brand">
        <span class="brand-dot"></span>
        <div class="brand-name">K.T.L Electrical<br>Services Pty Ltd</div>
      </div>
      <div class="brand-licence">EC 27418</div>
    </div>
    <div class="services">
      <p>Residential &amp; Commercial<span class="sep">•</span>Maintenance</p>
      <p>PV &amp; Battery servicing<span class="sep">•</span>EV Chargers</p>
    </div>
  </section>
</body>
</html>
```